Commercial Auto Insurance Application and Commercial Property Insurance Application

Hi I need a fillable application for my business to send to potential clients for Commercial Auto Insurance and Commercial Property Insurance. I have attached an example application I currently use for another line of insurance.
Commercial Auto Insurance Application
On the first page I would need the following:
- Business Name: (fill in area for text)
- Effective Date: (fill in area for text)
- How do you structure your business? (Check box for “Sole Proprietor”, “Partnership”, “Corporation”, “LLC”)
- Contact Name: (fill in area for text) / Phone Number: (fill in area for text) / Contact Email (fill in area for text)
- Mailing address: (fill in area for text)
- Garaging location: (fill in area for text)
- Owner Name: (fill in area for text)
- Description of Operations: (fill in area for text)
- How long has the operation been in business? (fill in area for text)
- How many years of experience does your management have in the truck/transportation industry? (fill in area for text)
Coverages
Liability Combined Single Limit: ($1,000,000 (checkbox) / $500,000 (checkbox / $300,000 (checkbox) / Other: (fill in area for text)
Uninsured Motorist CSL: (fill in area for text) (checkbox for “Rejected”)
Medical Payments: (fill in area for text)
Physical Damage: (fill in area for text) (checkbox for Rejected)
Liability Deducible: ($500 checkbox, $1,000 checkbox, $2,500 checkbox, $5,000 checkbox)
Physical Damage Deductible: ($500 checkbox, $1,000 checkbox, $2,500 checkbox, $5,000 checkbox)
Driving radius: (fill in area for text)
How many years have you had your own continuous commercial auto insurance coverage for the current business name? (fill in area for text)
Do any of your vehicles travel across state lines? Yes (checkbox)/ No (checkbox)
If yes, please list all states in which vehicles operate: (fill in area for text)
What is the maximum radius traveled for your customer's business?
0-25 miles (checkbox)
26-50 miles (checkbox)
51-75 miles (checkbox)
76-100 miles (checkbox)
101-150 miles (checkbox)
151-200 miles (checkbox)
201-300 miles (checkbox)
300+ miles (checkbox)
Would you like physical damage coverage for this vehicle? (should be for each vehicle listed)
On the 2nd page of the application I would need the following:
I would need to have it where people can fill in the vehicle information such as VIN:, Year:, Make:, Model:, Type of Vehicle:, Trailers:, Value:
I would also need to have it where people can fill in the drivers with their driver info including Name:, DOB:, DL #:, DL State:, Class of License:, Married: Yes/No, Number of years driving similar vehicle:
Please make it where you can fill in 20 vehicle's information and 20 driver's info.
For the 2nd Application I would need one for Property Insurance
On the Commercial Property Application I would need the following:
- Building Address: (fill in area for text)
- Building Description: (fill in area for text)
- Building Amount: $(fill in area for text)
- Business Personal Property Amount: $ (fill in area for text) (checkbox for Not Needed)
- Building Sq Ft: (fill in area for text)
- Total Area Sq Ft: (fill in area for text)
- Building Construction Type: Wood Frame (checkbox), Steel (checkbox), Fire Resistive (checkbox), Non-Combustible (checkbox), Other (fill in area for text)
- # of stories: (fill in area for text)
- Year Built: (fill in area for text)
- Wiring improvement year: (fill in area for text)
- Roofing improvement year: (fill in area for text)
- Plumbing improvement year: (fill in area for text)
- Heating improvement year: (fill in area for text)
- What is to the right of the building and distance: (fill in area for text)
- What is to the left of the building and distance: (fill in area for text)
- What is in front of the building and distance: (fill in area for text)
- What is behind the building and distance: (fill in area for text)
- Burglar alarm installation and serviced by: (fill in area for text) None (checkbox)
- Does the premises have fire protection? Sprinkler system (checkbox), Fire detection (checkbox), Other: (fill in area for text) None (checkbox)

```html
<!DOCTYPE html>
<html lang="en">
<head>
<meta charset="utf-8">
<title>Commercial Auto Insurance Application</title>
<link rel="stylesheet" href="https://fonts.googleapis.com/css2?family=Lato:wght@400;700;900&display=swap">
<style>
:root{
  --navy:#17358c;
  --shade:#e6ebf0;
  --line:#5a5a5a;
  --ink:#2a2a2a;
  --bg:#f5f5f5;
  --paper:#ffffff;
  --decor:#eef1f5;
}
*{box-sizing:border-box;margin:0;padding:0}
html,body{width:1200px;height:849px;overflow:hidden;background:var(--bg);font-family:'Lato',sans-serif;color:var(--ink)}
.page{position:absolute;top:128px;width:457px;height:592px;background:var(--paper);border:1px solid #d6d6d6}
.page-one{left:99px}
.page-two{left:644px}
.brand{position:absolute;left:15px;top:22px;display:flex;align-items:center;gap:5px;font-weight:900;font-size:22px;letter-spacing:.5px;color:var(--navy)}
.brand-mark{width:9px;height:9px;background:var(--navy)}
.office{position:absolute;right:8px;top:17px;text-align:right;font-size:6.8px;line-height:8.1px;color:#111}
.title{position:absolute;color:var(--navy);font-weight:700;font-size:14px;white-space:nowrap}
.page-one .title{left:13px;top:70px}
.page-two .title{right:9px;top:52px}
.section-label{position:absolute;font-weight:700;font-size:7.5px;color:#111}
.cell{position:absolute;border:.7px solid var(--line);font-size:4.8px;padding:3px 5px;line-height:1.3;background:var(--paper)}
.cell.shaded{background:var(--shade)}
.vr{position:absolute;top:0;bottom:0;border-left:.7px solid var(--line)}
.hr{position:absolute;left:0;right:0;border-top:.7px solid var(--line)}
.tick{display:inline-block;width:5px;height:5px;border:.6px solid #222;vertical-align:-1px;margin:0 4px 0 2px;background:#fff}
.micro{font-size:2.8px}
.row{position:absolute;left:0;right:0;height:16.4px;padding:5.5px 7px;border-top:.7px solid var(--line);white-space:nowrap}
.row:first-child{border-top:none}
.row.shaded{background:var(--shade)}
.options{position:absolute;font-size:4.6px;line-height:8px}
.options span{display:block;position:relative;width:38px}
.options .tick{position:absolute;right:0;top:1.5px;margin:0}
.decor{position:absolute;left:332px;top:454px;width:116px;height:114px;border-radius:10px;background:var(--decor)}
.grid{position:absolute;top:87px;border-collapse:collapse;table-layout:fixed;font-size:4.4px}
.grid th,.grid td{border:.7px solid var(--line);padding:0 3px}
.grid th{height:17px;text-align:left;font-weight:400;line-height:1.1;vertical-align:middle}
.grid td{height:23.05px}
.grid .s{background:var(--shade)}
.grid .tiny{font-size:3px}
.vehicles{left:13px;width:187px}
.drivers{left:233px;width:205px}
</style>
</head>
<body>

<section class="page page-one">
  <div class="brand"><span class="brand-mark"></span>RIDGEWAY</div>
  <div class="office">Ridgeway Insurance Services<br>4820 Meridian Ave Suite 110<br>Lakeview, CA 90521<br>Tel: (555) 014-2290</div>
  <h1 class="title">Commercial Auto Insurance Application</h1>

  <div class="cell" style="left:8px;top:95px;width:437px;height:16.5px;padding:5.5px 6px">Business Name:
    <span class="vr" style="left:302px"></span><span style="position:absolute;left:307px;top:5.5px">Effective Date:</span></div>
  <div class="cell shaded" style="left:8px;top:111px;width:437px;height:17px;padding:5.5px 6px">How do you structure your business?
    <span class="tick"></span>Sole Proprietor <span class="tick"></span>Partnership <span class="tick"></span>Corporation <span class="tick"></span>LLC</div>
  <div class="cell" style="left:8px;top:128px;width:437px;height:16.5px;padding:5.5px 6px">Contact Name:
    <span class="vr" style="left:142px"></span><span style="position:absolute;left:145px;top:5.5px">Phone Number:</span>
    <span class="vr" style="left:270px"></span><span style="position:absolute;left:275px;top:5.5px">Contact Email</span></div>
  <div class="cell shaded" style="left:8px;top:144px;width:437px;height:36px;padding:2px 6px">Mailing address:
    <span class="vr" style="left:218px"></span><span style="position:absolute;left:221px;top:2px">Mailing Location</span></div>

  <div class="cell" style="left:8px;top:182px;width:437px;height:59px;padding:0">
    <span style="position:absolute;left:6px;top:8px">Owner Name:</span>
    <span class="hr" style="top:16.5px;right:218px"></span>
    <span style="position:absolute;left:6px;top:23px">How long has the operation been in business?</span>
    <span class="vr" style="left:218px;bottom:23px"></span>
    <span style="position:absolute;left:221px;top:8px">Description of Operations:</span>
    <div class="row shaded" style="top:35.5px;height:23px;padding:7px 6px">How many years of experience does your management have in the truck/transportation industry?</div>
  </div>

  <h2 class="section-label" style="left:15px;top:245px">Coverages</h2>

  <div class="cell" style="left:8px;top:258px;width:213px;height:116px;padding:0">
    <div class="row" style="top:0">Liability Combined Single Limit: &nbsp;$1,000,000<span class="tick"></span> $500,000<span class="tick"></span> $300,000<span class="tick"></span></div>
    <div class="row shaded" style="top:16.4px">Other:</div>
    <div class="row" style="top:32.8px">Uninsured Motorist CSL:<span style="position:absolute;left:143px;top:5px"><span class="tick"></span><span class="micro">(Rejection)</span></span></div>
    <div class="row shaded" style="top:49.2px">Medical Payments:</div>
    <div class="row" style="top:65.6px">Physical Damage:<span style="position:absolute;left:145px;top:5px"><span class="tick"></span><span class="micro">(Rejection)</span></span></div>
    <div class="row shaded" style="top:82px">Liability Deductible:<span style="position:absolute;left:73px;top:5.5px">$500<span class="tick"></span>$1,000<span class="tick"></span>$2,500<span class="tick"></span>$5,000<span class="tick"></span></span></div>
    <div class="row" style="top:98.4px;padding-left:6px">Physical Damage Deductible:<span style="position:absolute;left:73px;top:5.5px">$500<span class="tick"></span>$1,000<span class="tick"></span>$2,500<span class="tick"></span>$5,000<span class="tick"></span></span></div>
  </div>
  <div class="cell shaded" style="left:8px;top:380px;width:213px;height:17px;font-size:7px;padding:3px 5px">Driving radius:</div>

  <div class="cell shaded" style="left:231px;top:258px;width:214px;height:35px;padding:3px 3px">How many years have you had your own continuous commercial auto insurance coverage for the current business name?</div>
  <div class="cell" style="left:231px;top:300px;width:214px;height:32px;padding:0">
    <span style="position:absolute;left:3px;top:4px">Do any of your vehicles travel across state lines? &nbsp;Yes<span class="tick" style="margin:0 3px 0 1px"></span>No<span class="tick" style="margin:0 1px"></span></span>
    <div class="row shaded" style="top:16px;height:15.5px;padding:4px 3px;font-style:italic;font-size:3.6px">If yes, please list all states in which vehicles operate:</div>
  </div>
  <div class="cell shaded" style="left:231px;top:340px;width:214px;height:57px;padding:3px 3px">What is the maximum radius traveled for your customer's business?
    <div class="options" style="left:3px;top:15px"><span>0-25 miles<i class="tick"></i></span><span>26-50 miles<i class="tick"></i></span><span>51-75 miles<i class="tick"></i></span><span>76-100 miles<i class="tick"></i></span></div>
    <div class="options" style="left:59px;top:15.5px"><span style="width:45px">101-150 miles<i class="tick"></i></span><span style="width:45px">151-200 miles<i class="tick"></i></span><span style="width:45px">201-300 miles<i class="tick"></i></span><span style="width:45px">300+ miles<i class="tick"></i></span></div>
    <span style="position:absolute;left:3px;top:48px">Would you like physical damage coverage for this vehicle?</span>
  </div>

  <div class="cell" style="left:8px;top:409px;width:437px;height:44px"></div>

  <div class="decor" role="img" aria-label="Faint outline icon of a car beneath a shield with a check mark"></div>
</section>

<section class="page page-two">
  <div class="brand"><span class="brand-mark"></span>RIDGEWAY</div>
  <div class="office">Ridgeway Insurance Services<br>4820 Meridian Ave Suite 110<br>Lakeview, CA 90521<br>Tel: (555) 014-2290</div>
  <h1 class="title">Commercial Auto Insurance Application</h1>
  <h2 class="section-label" style="left:13px;top:71px">Vehicle information</h2>
  <h2 class="section-label" style="left:233px;top:71px">Driver information</h2>

  <table class="grid vehicles">
    <colgroup><col style="width:43px"><col style="width:24px"><col style="width:24px"><col style="width:40px"><col style="width:28px"><col style="width:28px"></colgroup>
    <thead><tr><th class="s">VIN:</th><th>Year:</th><th class="s">Make:</th><th>Type of Vehicle:</th><th class="s">Trailers:</th><th>Value:</th></tr></thead>
    <tbody>
      <tr><td class="s"></td><td></td><td class="s"></td><td></td><td class="s"></td><td></td></tr>
      <tr><td class="s"></td><td></td><td class="s"></td><td></td><td class="s"></td><td></td></tr>
      <tr><td class="s"></td><td></td><td class="s"></td><td></td><td class="s"></td><td></td></tr>
      <tr><td class="s"></td><td></td><td class="s"></td><td></td><td class="s"></td><td></td></tr>
      <tr><td class="s"></td><td></td><td class="s"></td><td></td><td class="s"></td><td></td></tr>
      <tr><td class="s"></td><td></td><td class="s"></td><td></td><td class="s"></td><td></td></tr>
      <tr><td class="s"></td><td></td><td class="s"></td><td></td><td class="s"></td><td></td></tr>
      <tr><td class="s"></td><td></td><td class="s"></td><td></td><td class="s"></td><td></td></tr>
      <tr><td class="s"></td><td></td><td class="s"></td><td></td><td class="s"></td><td></td></tr>
      <tr><td class="s"></td><td></td><td class="s"></td><td></td><td class="s"></td><td></td></tr>
      <tr><td class="s"></td><td></td><td class="s"></td><td></td><td class="s"></td><td></td></tr>
      <tr><td class="s"></td><td></td><td class="s"></td><td></td><td class="s"></td><td></td></tr>
      <tr><td class="s"></td><td></td><td class="s"></td><td></td><td class="s"></td><td></td></tr>
      <tr><td class="s"></td><td></td><td class="s"></td><td></td><td class="s"></td><td></td></tr>
      <tr><td class="s"></td><td></td><td class="s"></td><td></td><td class="s"></td><td></td></tr>
      <tr><td class="s"></td><td></td><td class="s"></td><td></td><td class="s"></td><td></td></tr>
      <tr><td class="s"></td><td></td><td class="s"></td><td></td><td class="s"></td><td></td></tr>
      <tr><td class="s"></td><td></td><td class="s"></td><td></td><td class="s"></td><td></td></tr>
      <tr><td class="s"></td><td></td><td class="s"></td><td></td><td class="s"></td><td></td></tr>
      <tr><td class="s"></td><td></td><td class="s"></td><td></td><td class="s"></td><td></td></tr>
    </tbody>
  </table>

  <table class="grid drivers">
    <colgroup><col style="width:46px"><col style="width:31px"><col style="width:23px"><col style="width:23px"><col style="width:25px"><col style="width:28px"><col style="width:29px"></colgroup>
    <thead><tr><th class="s">Name:</th><th>DOB:</th><th class="s">DL #:</th><th>DL State:</th><th class="s">Class of License:</th><th>Married: Yes/No</th><th class="s tiny">Number of years driving similar vehicle:</th></tr></thead>
    <tbody>
      <tr><td class="s"></td><td></td><td class="s"></td><td></td><td class="s"></td><td></td><td class="s"></td></tr>
      <tr><td class="s"></td><td></td><td class="s"></td><td></td><td class="s"></td><td></td><td class="s"></td></tr>
      <tr><td class="s"></td><td></td><td class="s"></td><td></td><td class="s"></td><td></td><td class="s"></td></tr>
      <tr><td class="s"></td><td></td><td class="s"></td><td></td><td class="s"></td><td></td><td class="s"></td></tr>
      <tr><td class="s"></td><td></td><td class="s"></td><td></td><td class="s"></td><td></td><td class="s"></td></tr>
      <tr><td class="s"></td><td></td><td class="s"></td><td></td><td class="s"></td><td></td><td class="s"></td></tr>
      <tr><td class="s"></td><td></td><td class="s"></td><td></td><td class="s"></td><td></td><td class="s"></td></tr>
      <tr><td class="s"></td><td></td><td class="s"></td><td></td><td class="s"></td><td></td><td class="s"></td></tr>
      <tr><td class="s"></td><td></td><td class="s"></td><td></td><td class="s"></td><td></td><td class="s"></td></tr>
      <tr><td class="s"></td><td></td><td class="s"></td><td></td><td class="s"></td><td></td><td class="s"></td></tr>
      <tr><td class="s"></td><td></td><td class="s"></td><td></td><td class="s"></td><td></td><td class="s"></td></tr>
      <tr><td class="s"></td><td></td><td class="s"></td><td></td><td class="s"></td><td></td><td class="s"></td></tr>
      <tr><td class="s"></td><td></td><td class="s"></td><td></td><td class="s"></td><td></td><td class="s"></td></tr>
      <tr><td class="s"></td><td></td><td class="s"></td><td></td><td class="s"></td><td></td><td class="s"></td></tr>
      <tr><td class="s"></td><td></td><td class="s"></td><td></td><td class="s"></td><td></td><td class="s"></td></tr>
      <tr><td class="s"></td><td></td><td class="s"></td><td></td><td class="s"></td><td></td><td class="s"></td></tr>
      <tr><td class="s"></td><td></td><td class="s"></td><td></td><td class="s"></td><td></td><td class="s"></td></tr>
      <tr><td class="s"></td><td></td><td class="s"></td><td></td><td class="s"></td><td></td><td class="s"></td></tr>
      <tr><td class="s"></td><td></td><td class="s"></td><td></td><td class="s"></td><td></td><td class="s"></td></tr>
      <tr><td class="s"></td><td></td><td class="s"></td><td></td><td class="s"></td><td></td><td class="s"></td></tr>
    </tbody>
  </table>
</section>

</body>
</html>
```